CGSI application splash screen

We need a 1024x768 image for use as an application splash screen.
The image will be displayed full screen on an 10 inch industrial PC 1024x768 screen while our application is launching. The image should convey that the application is "Waiting for connection to Wi-Fi access point..." and include a graphic of the industrial PC connected to the access point via an Ethernet cable. A list of troubleshooting steps should be included at the bottom of the image. The troubleshooting steps should not be the main focus of the image and should be shown in a smaller font (but still readable at 1024x768 displayed on a 10 inch screen).
I will include a mock up of the general idea of what we are looking for as well as image files for the industrial PC, a screenshot of our application to show on the PC's screen and the AP.
For general look and feel and a sense of corporate branding please review our website https://copperlanegrowingsystems.com/. The splash screen should reflect corporate branding.
Users of our application
Agriculture

```html
<!DOCTYPE html>
<html lang="en">
<head>
<meta charset="utf-8">
<title>Copper Lane Growing Systems – Waiting for Wi-Fi access point</title>
<link rel="stylesheet" href="https://fonts.googleapis.com/css2?family=Barlow:wght@400;500;600&display=swap">
<style>
  :root {
    --brand-green: #2bb673;
    --brand-green-light: #4cc488;
    --paper: #ffffff;
    --device-body: #24272a;
    --device-screen: #dfe7e2;
    --ap-body: #f1f2f2;
    --cable: #1a1a1a;
    --text-light: #ffffff;
  }
  * { margin: 0; padding: 0; box-sizing: border-box; }
  html, body { width: 1200px; height: 900px; overflow: hidden; }
  body { font-family: "Barlow", sans-serif; background: var(--paper); }

  .splash { position: relative; width: 1200px; height: 900px; overflow: hidden; background: var(--brand-green); }
  .splash-backdrop { position: absolute; inset: 0; }

  .status-title {
    position: absolute; left: 20px; top: 24px; width: 770px;
    color: var(--text-light); font-weight: 500; font-size: 78px; line-height: 94px;
    text-align: center; letter-spacing: 0.5px; white-space: nowrap;
  }

  .cab-computer {
    position: absolute; left: 91px; top: 387px; width: 316px; height: 246px;
    background: var(--device-body); border-radius: 12px;
  }
  .cab-computer-screen {
    position: absolute; left: 30px; top: 24px; width: 256px; height: 186px;
    background: var(--device-screen); border-radius: 2px;
  }
  .ap-unit {
    position: absolute; left: 1034px; top: 111px; width: 62px; height: 410px;
    background: linear-gradient(90deg, #ffffff, var(--ap-body) 60%, #d9dcdc);
    border-radius: 10px;
  }

  .device-label { position: absolute; font-weight: 500; text-align: center; }
  .device-label--computer { left: 96px; top: 646px; width: 300px; color: var(--brand-green); font-size: 22px; }
  .device-label--ap { left: 960px; top: 612px; width: 200px; color: var(--text-light); font-size: 20px; font-weight: 600; line-height: 24px; }

  .troubleshooting { position: absolute; left: 64px; top: 713px; color: var(--text-light); font-size: 14.5px; line-height: 19px; }
  .troubleshooting-heading { font-weight: 500; font-size: 15px; margin-bottom: 9px; }
  .steps { list-style: none; }
  .steps > li { position: relative; padding-left: 22px; font-weight: 400; }
  .steps > li::before { content: "➤"; position: absolute; left: 0; top: 0; font-size: 13px; }
  .substeps { list-style: none; }
  .substeps li { position: relative; padding-left: 17px; }
  .substeps li::before { content: "➡"; position: absolute; left: 0; top: 0; font-size: 12px; }

  .brand-name {
    position: absolute; left: 960px; top: 740px; width: 200px;
    color: var(--text-light); font-weight: 600; font-size: 26px; line-height: 30px;
    text-align: center;
  }
</style>
</head>
<body>
<main class="splash">
  <svg class="splash-backdrop" width="1200" height="900" viewBox="0 0 1200 900" aria-hidden="true">
    <path d="M0,314 L640,314 C740,314 790,210 835,145 C860,110 885,94 914,94 L914,697 L0,697 Z" fill="var(--paper)"/>
    <path d="M914,94 C960,88 1060,86 1200,86" fill="none" stroke="var(--brand-green-light)" stroke-width="3"/>
    <path d="M407,586 L1000,586 C1055,586 1064,566 1064,521" fill="none" stroke="var(--cable)" stroke-width="5" stroke-linecap="round"/>
  </svg>

  <h1 class="status-title">Waiting for<br>connection to Wi-Fi<br>access point...</h1>

  <div class="cab-computer" role="img" aria-label="Industrial tractor cab computer showing the seeding application screen">
    <div class="cab-computer-screen"></div>
  </div>
  <div class="ap-unit" role="img" aria-label="Outdoor Wi-Fi access point with two antennas"></div>

  <p class="device-label device-label--computer">Tractor Cab Computer</p>
  <p class="device-label device-label--ap">Wi-Fi Access<br>Point</p>

  <section class="troubleshooting">
    <h2 class="troubleshooting-heading">Troubleshooting steps:</h2>
    <ul class="steps">
      <li>This screen should only be visible for a short time on boot.</li>
      <li>If this screen stays visible for more than a minute:
        <ul class="substeps">
          <li>Verify that the Wi-Fi Access Point (AP) powers up when this system does (indicated by a green light on the side of the AP).</li>
          <li>Check the Ethernet cable between this system and the AP for damage, and replace it if necessary.</li>
          <li>Power-cycle this system and wait for it to reboot fully.</li>
          <li>If the issue persists, contact CGSI support for further assistance.</li>
        </ul>
      </li>
    </ul>
  </section>

  <p class="brand-name">Copper Lane<br>Growing<br>Systems</p>
</main>
</body>
</html>
```